Critter Wardens Door Hanger

For the right side, we would like to take out the scorpion and 2 butterflies and replace with a mouse, rat, and squirrel.
Take out Bugbane Z and Q Bright Pest Control and replace with a logo. Our company name is Critter Wardens - if you can design it with a Commander Falconridge shield from the Stormguard, maybe with a raccoon chewing or shooting at a wasp nest.
At bottom, please write Call/Text/Email for a free quote
555-201-3964, critterwardens@fernmail.net
Please do same for the other side on bottom.

For the left side, if you can change the bedbug red shadow frame to a mouse or rats. Within the sillhouette, If you can please replace bees with rats. Please also replace Call for a quote today, to " Support Your Small Locally Owned Family Business".

For the gray text, please change to " We want your business. (bold) Willing to match or beat any competitors price by 10 % or more guaranteed , must show proof of invoice". (smaller font)

```html
<!DOCTYPE html>
<html lang="en">
<head>
<meta charset="utf-8">
<title>Critter Wardens Door Hanger</title>
<link rel="stylesheet" href="https://fonts.googleapis.com/css2?family=Archivo+Black&family=Great+Vibes&family=Montserrat:wght@400;800&family=Roboto:wght@400;500;700&family=Roboto+Condensed:wght@700&display=swap">
<style>
  :root {
    --canvas: #dedede;
    --pattern-front: #2b1510;
    --pattern-front-2: #1a1110;
    --pattern-back: #4a1a10;
    --pattern-back-2: #1d1210;
    --orange: #e8501f;
    --orange-bright: #f23a00;
    --phone: #ee3a0a;
    --white: #ffffff;
    --text-dark: #1a1a1a;
  }
  * { box-sizing: border-box; margin: 0; padding: 0; }
  html, body { width: 1070px; height: 1200px; overflow: hidden; }
  body { background: var(--canvas); position: relative; font-family: "Roboto", Arial, sans-serif; }

  .hanger {
    position: absolute;
    width: 368px;
    height: 955px;
    background: var(--white);
  }
  .hanger--front {
    left: 143px; top: 130px;
    clip-path: path("M0,20 Q0,0 20,0 H348 Q368,0 368,20 V955 H0 V172 Q0,152 20,152 H104 A81 81 0 1 0 104,137 H20 Q0,137 0,117 Z");
  }
  .hanger--back {
    left: 569px; top: 132px;
    clip-path: path("M20,0 H348 Q368,0 368,20 V117 Q368,137 348,137 H266 A81 81 0 1 0 266,152 H348 Q368,152 368,172 V935 Q368,955 348,955 H20 Q0,955 0,935 V20 Q0,0 20,0 Z");
  }

  .pattern { position: absolute; left: 0; top: 0; width: 100%; }
  .hanger--front .pattern { height: 752px; background: linear-gradient(160deg, var(--pattern-front), var(--pattern-front-2) 60%, var(--pattern-front)); }
  .hanger--back .pattern { height: 615px; background: linear-gradient(160deg, var(--pattern-back), var(--pattern-back-2) 55%, var(--pattern-back)); }

  .rat-badge {
    position: absolute; left: 142px; top: 228px; width: 226px; height: 150px;
    background: var(--orange);
    border-radius: 90px 0 0 70px / 60px 0 0 90px;
  }
  .pest-list {
    position: absolute; left: 218px; top: 254px; width: 150px;
    text-align: center; color: var(--white);
    font-size: 11.5px; line-height: 12.8px;
  }
  .pest-list__title { font-family: "Archivo Black", sans-serif; font-size: 11px; line-height: 12.5px; }

  .headline {
    position: absolute; left: 0; width: 100%; top: 380px;
    text-align: center; color: var(--white);
    font-family: "Archivo Black", sans-serif; font-size: 30px; line-height: 34px; letter-spacing: -0.5px;
  }
  .match-ribbon {
    position: absolute; left: 56px; top: 460px; width: 254px; height: 46px;
    background: var(--orange-bright); transform: rotate(-2deg);
    color: var(--white); font-family: "Roboto Condensed", sans-serif; font-weight: 700;
    font-size: 27px; line-height: 46px; text-align: center; letter-spacing: -0.3px;
  }
  .or-script {
    position: absolute; left: 0; width: 100%; top: 510px; text-align: center;
    color: var(--white); font-family: "Great Vibes", cursive; font-size: 40px; line-height: 40px;
  }
  .guarantee {
    position: absolute; left: 0; width: 100%; top: 554px; text-align: center;
    color: var(--white); font-family: "Roboto Condensed", sans-serif; font-weight: 700;
    font-size: 17.5px; line-height: 20.5px; letter-spacing: -0.4px;
  }

  .brand {
    position: absolute; left: 0; width: 100%;
    display: flex; justify-content: center; align-items: center; gap: 10px;
    font-family: "Montserrat", sans-serif; font-weight: 800;
    font-size: 27px; line-height: 34px; letter-spacing: 0.5px; text-transform: uppercase;
  }
  .hanger--front .brand { top: 672px; color: var(--white); }
  .hanger--back .brand { top: 672px; color: var(--text-dark); }
  .brand__mark { width: 16px; height: 16px; border-radius: 50%; background: var(--orange-bright); flex: none; }

  .contact { position: absolute; left: 0; width: 100%; text-align: center; }
  .hanger--front .contact { top: 765px; }
  .hanger--back .contact { top: 755px; }
  .contact__cta { font-family: "Montserrat", sans-serif; font-weight: 800; font-size: 23px; line-height: 30px; color: var(--text-dark); }
  .contact__note { font-size: 15px; line-height: 20px; color: var(--text-dark); letter-spacing: -0.3px; }
  .contact__phone {
    margin-top: 7px; display: flex; justify-content: center; align-items: center; gap: 14px;
    color: var(--phone); font-weight: 700; font-size: 30px; line-height: 34px;
  }
  .contact__email {
    margin-top: 4px; display: flex; justify-content: center; align-items: center; gap: 6px;
    font-size: 17px; line-height: 24px; color: var(--text-dark);
  }
  .support-button {
    margin: 12px auto 0; width: 242px; height: 39px; background: var(--orange-bright);
    color: var(--white); font-weight: 700; font-size: 13px; line-height: 15px; letter-spacing: -0.3px;
    display: flex; align-items: center; justify-content: center; text-align: center;
  }
</style>
</head>
<body>

<section class="hanger hanger--front" aria-label="Door hanger front">
  <div class="pattern" role="img" aria-label="Repeating pattern of rat, mouse and squirrel silhouettes"></div>
  <div class="rat-badge" role="img" aria-label="Large orange rat silhouette"></div>
  <div class="pest-list">
    <div class="pest-list__title">WE CAN<br>DEAL WITH...</div>
    Mice, Cockroaches,<br>Hornets, Fleas, Bees,<br>Wasps, Bedbugs, Flies<br>Ants, Carpenter Ants.
  </div>
  <h1 class="headline">WE WANT<br>YOUR BUSINESS</h1>
  <div class="match-ribbon">WILLING TO MATCH</div>
  <div class="or-script">Or</div>
  <p class="guarantee">BEAT ANY COMPETITORS PRICE<br>BY 10 % OR MORE GUARANTEED,<br>MUST SHOW PROOF OF INVOICE</p>
  <div class="brand"><span class="brand__mark"></span><span>Critter Wardens</span></div>
  <div class="contact">
    <div class="contact__cta">CALL NOW</div>
    <div class="contact__note">Call/Text/Email for a free quote</div>
    <div class="contact__phone">
      <svg width="20" height="20" viewBox="0 0 24 24" aria-hidden="true"><path fill="currentColor" d="M6.6 10.8c1.4 2.8 3.8 5.1 6.6 6.6l2.2-2.2c.3-.3.7-.4 1-.2 1.1.4 2.3.6 3.6.6.6 0 1 .4 1 1V20c0 .6-.4 1-1 1C10.6 21 3 13.4 3 4c0-.6.4-1 1-1h3.5c.6 0 1 .4 1 1 0 1.3.2 2.5.6 3.6.1.3 0 .7-.2 1l-2.3 2.2z"/></svg>
      <span>555-201-3964</span>
    </div>
    <div class="contact__email">
      <svg width="11" height="16" viewBox="0 0 11 16" aria-hidden="true"><path fill="currentColor" d="M0 0 L0 13 L3.2 10 L5.5 15.5 L7.6 14.6 L5.3 9.2 L9.8 9.2 Z"/></svg>
      <span>critterwardens@fernmail.net</span>
    </div>
    <div class="support-button">Support Your Small<br>Locally Owned Family Business</div>
  </div>
</section>

<section class="hanger hanger--back" aria-label="Door hanger back">
  <div class="pattern" role="img" aria-label="Repeating pattern of rat, mouse and squirrel silhouettes"></div>
  <div class="brand"><span class="brand__mark"></span><span>Critter Wardens</span></div>
  <div class="contact">
    <div class="contact__cta">CALL NOW</div>
    <div class="contact__note">Call/Text/Email for a free quote</div>
    <div class="contact__phone">
      <svg width="20" height="20" viewBox="0 0 24 24" aria-hidden="true"><path fill="currentColor" d="M6.6 10.8c1.4 2.8 3.8 5.1 6.6 6.6l2.2-2.2c.3-.3.7-.4 1-.2 1.1.4 2.3.6 3.6.6.6 0 1 .4 1 1V20c0 .6-.4 1-1 1C10.6 21 3 13.4 3 4c0-.6.4-1 1-1h3.5c.6 0 1 .4 1 1 0 1.3.2 2.5.6 3.6.1.3 0 .7-.2 1l-2.3 2.2z"/></svg>
      <span>555-201-3964</span>
    </div>
    <div class="contact__email">
      <svg width="11" height="16" viewBox="0 0 11 16" aria-hidden="true"><path fill="currentColor" d="M0 0 L0 13 L3.2 10 L5.5 15.5 L7.6 14.6 L5.3 9.2 L9.8 9.2 Z"/></svg>
      <span>critterwardens@fernmail.net</span>
    </div>
    <div class="support-button">Support Your Small<br>Locally Owned Family Business</div>
  </div>
</section>

</body>
</html>
```